swimming pool Leak Detection Brochure

I would Like to create a pool leak detection brochure

Target Market(s)

High end Clients with inground swimming pools

Industry/Entity Type

Pool Service

Other font styles liked:
• Im open to suggestions but using my website for ideas is suggested

Colors

Designer to choose colors to be used in the design.

Requirements
Must have
• Do you Have a Leak??
• Figuring out when your pool has a leak can be tough. Environmental factors do play a role in the water level, and just because your pool’s water is lower than normal does not mean it has a leak. Wind, humidity, and sun exposure all impact your rate of evaporation.
• Warning Signs of a Leak in Your Pool
• Your pool, fountain, or spa loses more than 1/4 an inch of water a day
• There are cracks in or around the pool decking
• You need to add water more than once a week
• Grass around the area is soggy
• Your pool deck is sinking or lifting
Nice to have
• PREPARING FOR A LEAK TEST
• To ensure you receive an accurate leak detection test, it is required that you have the pool vacuumed and cleaned beforehand. Dirt and debris in the pool can make it difficult to spot even large leaks. Likewise, the water should be as clear as possible. If your water is green it means mildew, algae, or fungi has infested it. Not only does this make it impossible to test for leaks, but it’s dangerous for our health. Finally our pool should be full to the normal level - we can’t find a leak that is not leaking! After your test, you will be confident knowing you have a pool/fountain/spa that is free of leaks or the Leak has been found and can be repaired Properly.

```html
<!DOCTYPE html>
<html lang="en">
<head>
<meta charset="utf-8">
<title>Harborline Pool Service – Leak Detection Brochure</title>
<link rel="stylesheet" href="https://fonts.googleapis.com/css2?family=Permanent+Marker&family=Open+Sans:ital,wght@0,400;0,600;0,700;1,700&display=swap">
<style>
:root{
  --bg:#2e2f31;
  --paper:#ffffff;
  --paper-shade:#eef0f4;
  --ink:#222428;
  --body:#3a3d42;
  --blue:#3a8ed8;
  --orange:#d1662a;
  --orange-dark:#b9531d;
  --rule:#2f6fb6;
  --silver:#c9cdd3;
  --partner:#4a4f57;
}
*{box-sizing:border-box;margin:0;padding:0}
html,body{width:1200px;height:789px;overflow:hidden}
body{background:var(--bg);font-family:"Open Sans",Arial,sans-serif;color:var(--body)}
.spread{position:absolute;left:40px;top:24px;width:1120px;height:740px;display:flex;box-shadow:0 12px 30px rgba(0,0,0,.45)}
.page{position:relative;width:560px;height:740px;background:linear-gradient(90deg,var(--paper) 85%,var(--paper-shade));overflow:hidden}
.page--right{background:linear-gradient(90deg,var(--paper-shade),var(--paper) 12%)}
.band{position:absolute;inset:0;width:560px;height:740px}
.content{position:absolute;left:48px;right:40px}
.marker{font-family:"Permanent Marker","Comic Sans MS",cursive;text-transform:uppercase;line-height:1.15;letter-spacing:1px;font-weight:400}
.marker .accent{color:var(--blue)}
.section-head{font-size:24px;color:var(--ink);padding-bottom:5px;border-bottom:2px solid var(--rule);display:inline-block;padding-right:20px}
.intro-list{list-style:none;margin-top:10px;font-size:10.5px;line-height:1.4}
.intro-list li{position:relative;padding-left:18px}
.intro-list li::before{content:"";position:absolute;left:2px;top:3px;width:8px;height:4px;border-left:2px solid var(--orange);border-bottom:2px solid var(--orange);transform:rotate(-45deg)}
.copy{font-size:10.5px;line-height:1.45;text-align:justify;margin-top:10px}
.page--left .copy{line-height:1.4}
.partners{position:absolute;left:48px;top:418px;width:260px;display:flex;flex-wrap:wrap;gap:4px 16px}
.partner{font-size:12px;font-weight:700;color:var(--partner)}
.phone{position:absolute;left:48px;top:645px;color:#fff;font-weight:700;font-size:26px;display:flex;align-items:center;gap:14px;letter-spacing:1px}
.phone svg{width:22px;height:22px}
.photo{position:absolute;border-radius:50%;border:6px solid #fff;box-shadow:0 0 0 3px var(--orange)}
.photo--kit{left:325px;top:495px;width:160px;height:160px;background:radial-gradient(circle at 50% 45%,#6c7078,#cfd2d7 70%)}
.photo--float{left:70px;top:510px;width:145px;height:145px;background:linear-gradient(180deg,#7fb4e0 0%,#e8d23a 45%,#2a7fc0 75%)}
.photo--deck{left:300px;top:515px;width:175px;height:175px;background:linear-gradient(180deg,#b9cfe6 0%,#e9edf1 45%,#4aa7d8 75%)}
.ring{position:absolute;border-radius:50%;border:2px solid var(--blue);border-left-color:transparent;border-bottom-color:transparent}
.title{font-size:28px;color:var(--blue)}
.company{font-size:15px;font-weight:700;color:var(--ink);margin-top:16px;padding-bottom:4px;border-bottom:2px solid var(--rule)}
.company span{font-weight:400}
.benefits{font-size:14px;font-weight:700;color:var(--ink);margin-top:14px;padding-bottom:4px;border-bottom:2px solid var(--rule);display:inline-block;padding-right:30px}
.promise{margin-top:12px;color:var(--blue);font-weight:700;font-size:12.5px;line-height:1.4}
.web{position:absolute;right:40px;bottom:36px;color:#fff;font-size:16px;display:flex;align-items:center;gap:10px}
.web b{font-weight:700}
.web svg{width:16px;height:16px}
</style>
</head>
<body>
<main class="spread">
  <section class="page page--left">
    <svg class="band" viewBox="0 0 560 740" aria-hidden="true">
      <path d="M0 478 C160 470 330 520 560 540 L560 740 L0 740 Z" fill="var(--orange)"/>
      <path d="M0 505 C160 495 330 540 560 560" fill="none" stroke="var(--silver)" stroke-width="7"/>
      <path d="M0 660 C200 710 400 700 560 675 L560 740 L0 740 Z" fill="var(--orange-dark)" opacity=".35"/>
    </svg>
    <div class="content" style="top:30px">
      <h2 class="marker section-head">Do you have a <span class="accent">Leak??</span></h2>
      <ul class="intro-list">
        <li>Figuring out when your pool has a leak can be tough. Environmental factors do play a role in the water level, and just because your pool's water is lower than normal does not mean it has a leak. Wind, humidity, and sun exposure all impact your rate of evaporation.</li>
        <li>Warning Signs of a Leak in Your Pool</li>
        <li>Your pool, fountain, or spa loses more than 1/4 an inch of water a day</li>
        <li>There are cracks in or around the pool decking</li>
        <li>You need to add water more than once a week</li>
        <li>Grass around the area is soggy</li>
        <li>Your pool deck is sinking or lifting</li>
      </ul>
      <h2 class="marker section-head" style="margin-top:14px">Preparing for a <span class="accent">Leak Test?</span></h2>
      <p class="copy">To ensure you receive an accurate leak detection test, it is required that you have the pool vacuumed and cleaned beforehand. Dirt and debris in the pool can make it difficult to spot even large leaks. Likewise, the water should be as clear as possible. If your water is green it means mildew, algae, or fungi has infested it. Not only does this make it impossible to test for leaks, but it's dangerous for our health. Finally our pool should be full to the normal level - we can't find a leak that is not leaking! After your test, you will be confident knowing you have a pool/fountain/spa that is free of leaks or the Leak has been found and can be repaired Properly.</p>
    </div>
    <div class="partners">
      <span class="partner">Coverline</span>
      <span class="partner">PureBalance</span>
      <span class="partner">DeepSweep</span>
      <span class="partner">Tidewell</span>
      <span class="partner">Aquaron</span>
      <span class="partner">FlowMark</span>
      <span class="partner">Heatwave</span>
    </div>
    <div class="ring" style="left:310px;top:480px;width:190px;height:190px"></div>
    <div class="photo photo--kit" role="img" aria-label="Photo of an open leak detection equipment case with hoses and tools"></div>
    <div class="phone">
      <svg viewBox="0 0 24 24" aria-hidden="true"><circle cx="12" cy="12" r="10.5" fill="none" stroke="#fff" stroke-width="2"/><path d="M9 7c-1 .5-1.5 1.5-1 3 .8 2.5 2.5 4.3 5 5.5 1.4.6 2.5 0 3-1l-2-1.6-1.2.8c-1.2-.6-2.2-1.6-2.8-2.8l.8-1.2Z" fill="#fff"/></svg>
      401-555-0147
    </div>
  </section>

  <section class="page page--right">
    <svg class="band" viewBox="0 0 560 740" aria-hidden="true">
      <path d="M0 530 C140 570 320 600 560 530 L560 740 L0 740 Z" fill="var(--orange)"/>
      <path d="M0 555 C140 595 320 622 560 555" fill="none" stroke="var(--silver)" stroke-width="6"/>
    </svg>
    <div class="content" style="top:38px">
      <h1 class="marker title">Pool Maintenance,<br>Cleaning, &amp; Repairs in RI</h1>
      <p class="company">HARBORLINE POOL SERVICE <span>RI, MA, CT</span></p>
      <p class="copy">Serving Massachusetts, Rhode Island, including Block Island and Connecticut, Harborline Pool Service stands ready to provide exceptional pool maintenance for the swimming pool at your home or on your commercial property. Whether it's a high-end vacation resort, hotel, apartment complex or a private residence, Harborline Pool Service can provide pool cleaning, repair and maintenance of pools anywhere in RI.</p>
      <h3 class="benefits">Benefits of Harborline Pool Service</h3>
      <p class="copy">As a family owned and operated small business the founder of Harborline Pool Service, Daniel Crane is sure to spend extra time with each customer to better serve them. While the "big boys" may have more representatives, they are always ready to move on to the next transaction.</p>
      <p class="copy" style="margin-top:6px">We have always strived to provide a high level of pool service at the initial stages of a transaction as well as after the job is complete. We want you to love your pool by having it cleaned and properly maintained on a regular basis.</p>
      <p class="promise">Your satisfaction is GUARANTEED.<br>For Pool Repair, Maintenance, and Cleaning<br>Call Harborline Pool Service TODAY!!!!</p>
    </div>
    <div class="ring" style="left:55px;top:495px;width:175px;height:175px"></div>
    <div class="photo photo--float" role="img" aria-label="Photo of an inflatable float in an infinity pool overlooking the sea"></div>
    <div class="ring" style="left:284px;top:499px;width:207px;height:207px"></div>
    <div class="photo photo--deck" role="img" aria-label="Photo of a technician servicing a rooftop pool"></div>
    <div class="web">
      <svg viewBox="0 0 24 24" aria-hidden="true"><circle cx="12" cy="12" r="10" fill="none" stroke="#fff" stroke-width="2"/><path d="M2 12h20M12 2c3 3 3 17 0 20M12 2c-3 3-3 17 0 20" fill="none" stroke="#fff" stroke-width="1.6"/></svg>
      <span>www.<b>harborlinepools</b>.com</span>
    </div>
  </section>
</main>
</body>
</html>
```